Flyer Design Project

I teach a spiritual dance class and I want to explain what it is and who it would benefit. I would love to have a sticker for where I am teaching it because that can change.

I want it to be a bit spiritual, very hip and cool, and transformational!!

Target Market(s)

Mostly women (or enlightened men)! all ages

Requirements
Must have
• Lumen Sway

We need to move. We need to breathe. We need to smile and giggle and laugh and cry and scream and make noise and dance. It's not about burning calories and it is not about reaching a goal. It's about feeling. It's about taking the time to nurture our souls. It's about finding joy and peace in our hectic lives. It's about healing.

Lumen Sway is a wildly fun, uplifting, emotionally cleansing, refreshing, restorative, heart-opening, transformational dance celebration that is sure to leave you relaxed and smiling. All ages, shapes and sizes are welcome with no experience necessary.
About Carla:

I was certified at Vestora in both “Open Heart Motion Flow” and “Tidal Steps” and am a
certified Group Exercise Instructor with the National Council for Active Movement Trainers (NCAM). I also have a black belt in Tae Kwon Do. As of 2013, I will be a certified holistic health and nutrition coach and am the creator of the popular Bright, Bold, and Breezy page on Friendloop.
For more info:
Carlabrennick@mailvista.net

Classes and workshops to energize your body, mind, and spirit.

```html
<!DOCTYPE html>
<html lang="en">
<head>
<meta charset="utf-8">
<title>Lumen Sway — Dance Flyer</title>
<link rel="stylesheet" href="https://fonts.googleapis.com/css2?family=Sacramento&family=Parisienne&family=Didact+Gothic&display=swap">
<style>
  :root {
    --page: #ffffff;
    --paper-top: #dedede;
    --paper-bottom: #fbfbfb;
    --ink-blue: #2b2fc9;
    --ink-dark: #333333;
    --ink-lavender: #b9b4f2;
    --sky-light: #dfe6ee;
    --sky-mid: #aebfd0;
    --rock-blue: #5f7a99;
    --white: #ffffff;
  }
  * { box-sizing: border-box; margin: 0; padding: 0; }
  html, body {
    width: 934px; height: 1200px; overflow: hidden;
    background: var(--page);
  }
  .flyer {
    position: absolute; left: 141px; top: 140px;
    width: 652px; height: 921px;
    background: linear-gradient(160deg, var(--paper-top) 0%, #e9e9e9 35%, var(--paper-bottom) 62%);
    border: 1px solid #c8c8c8;
    overflow: hidden;
    font-family: "Didact Gothic", sans-serif;
  }
  .flyer__title {
    position: absolute; left: 0; right: 0; top: 0;
    text-align: center;
    font-family: "Sacramento", cursive;
    font-weight: 400;
    font-size: 112px; line-height: 1.05;
    color: var(--ink-blue);
    padding-left: 60px;
  }
  .intro {
    position: absolute; left: 15px; top: 124px; width: 309px;
    text-align: justify;
    color: var(--ink-dark);
  }
  .intro__lead {
    font-size: 24.5px; line-height: 31px; color: var(--ink-blue);
  }
  .intro__body { font-size: 14px; line-height: 20px; }
  .intro__desc {
    margin-top: 20px; font-size: 14px; line-height: 20px;
  }
  .about {
    position: absolute; left: 337px; top: 124px; width: 304px;
  }
  .about__heading {
    font-family: "Parisienne", cursive; font-weight: 400;
    font-size: 26px; line-height: 32px; color: var(--ink-dark);
    margin-bottom: 8px;
  }
  .about__text {
    font-size: 14px; line-height: 20px; text-align: justify;
    color: var(--ink-lavender);
  }
  .contact {
    position: absolute; right: 18px; top: 428px; text-align: right;
  }
  .contact__label { font-size: 23px; line-height: 30px; color: var(--ink-dark); }
  .contact__email { font-size: 27px; line-height: 40px; color: var(--ink-blue); }
  .hero {
    position: absolute; left: 0; right: 0; top: 518px; bottom: 0;
    background: linear-gradient(180deg, var(--sky-light) 0%, var(--sky-mid) 45%, #8ea4bc 72%, var(--rock-blue) 100%);
  }
  .hero__tagline {
    position: absolute; left: 18px; top: 16px; width: 620px;
    font-family: "Parisienne", cursive; font-weight: 400;
    font-size: 42px; line-height: 52px; color: var(--white);
  }
</style>
</head>
<body>
  <main class="flyer">
    <h1 class="flyer__title">Lumen Sway</h1>

    <section class="intro">
      <p class="intro__body"><span class="intro__lead">We need to move. We need to breathe. We need to smile and giggle and laugh and cry and scream and make noise and dance.</span> It's not about burning calories and it is not about reaching a goal. It's about feeling. It's about taking the time to nurture our souls. It's about finding joy and peace in our hectic lives. It's about healing.</p>
      <p class="intro__desc">Lumen Sway is a wildly fun, uplifting, emotionally cleansing, refreshing, restorative, heart-opening, transformational dance celebration that is sure to leave you relaxed and smiling. All ages, shapes and sizes are welcome with no experience necessary.</p>
    </section>

    <section class="about">
      <h2 class="about__heading">About Carla:</h2>
      <p class="about__text">I was certified at Vestora in both "Open Heart Motion Flow" and "Tidal Steps" and am a certified Group Exercise Instructor with the National Council for Active Movement Trainers (NCAM). I also have a black belt in Tae Kwon Do. As of 2013, I will be a certified holistic health and nutrition coach and am the creator of the popular Bright, Bold, and Breezy page on Friendloop.</p>
    </section>

    <div class="contact">
      <p class="contact__label">For more info:</p>
      <p class="contact__email">Carlabrennick@mailvista.net</p>
    </div>

    <section class="hero" role="img" aria-label="Photo of a dancer in a blue dress balancing on a rocky cliff beside a cluster of lavender balloons under a hazy sky">
      <p class="hero__tagline">Classes and workshops to energize your body, mind, and spirit.</p>
    </section>
  </main>
</body>
</html>
```